Cedar Brook Stables, LLC

Equestrian business card to promote equine retirement, farm sitting, short term board. Located in Aiken, SC.
Updated color schemes.
Contact Information for Business Card
Contact info, description of work.
Colors
0094D4
00A9DD
6FCCEA
C7EBF8
E9F6FB
59FF00
82FF00
B8FF75
E3FFCB
F4FFEA
F0912C
F2A743
F7CA91
FBE8D2
FDF5EE

```html
<!DOCTYPE html>
<html lang="en">
<head>
<meta charset="utf-8">
<title>Cedar Brook Stables – Business Card</title>
<link rel="stylesheet" href="https://fonts.googleapis.com/css2?family=Cinzel:wght@700&family=Arimo:wght@400;700&display=swap">
<style>
  :root {
    --blue: #0094D4;
    --green: #59FF00;
    --green-soft: #82FF00;
    --orange: #F0912C;
    --orange-light: #FBE8D2;
    --ink: #1a1a1a;
    --paper: #ffffff;
    --backdrop: #ececec;
  }
  * { margin: 0; padding: 0; box-sizing: border-box; }
  html, body { width: 910px; height: 1200px; overflow: hidden; }
  body { background: var(--backdrop); position: relative; font-family: "Arimo", Arial, sans-serif; }

  .card {
    position: absolute; left: 75px; width: 760px; height: 455px;
    background: var(--paper); overflow: hidden;
    box-shadow: 0 6px 18px rgba(0,0,0,.18);
  }
  .card--front { top: 90px; }
  .card--back { top: 650px; }
  .card__shapes { position: absolute; inset: 0; width: 760px; height: 455px; }

  .brand {
    position: absolute; text-align: center;
    font-family: "Cinzel", Georgia, serif; font-weight: 700;
    color: var(--blue); line-height: 1.15;
  }
  .brand__dot {
    display: block; width: 34px; height: 34px; border-radius: 50%;
    background: var(--orange); margin: 0 auto 14px;
  }
  .card--front .brand { left: 48px; top: 120px; width: 290px; font-size: 30px; }
  .card--back .brand { left: 215px; top: 150px; width: 330px; font-size: 34px; }

  .person { position: absolute; right: 55px; top: 112px; text-align: right; }
  .person__name { font-family: "Cinzel", Georgia, serif; font-weight: 700; font-size: 25px; color: var(--ink); letter-spacing: .5px; }
  .person__role { font-size: 18px; color: var(--ink); margin-top: 8px; }

  .divider {
    position: absolute; left: 480px; top: 198px; width: 280px; height: 4px;
    background: linear-gradient(to right, rgba(89,255,0,0), var(--green-soft) 60%);
  }

  .contact { position: absolute; left: 520px; font-size: 18px; color: var(--ink); line-height: 1.3; }
  .contact svg { position: absolute; left: 0; top: 3px; width: 20px; height: 20px; }
  .contact__text { padding-left: 36px; display: block; }
  .contact--address { top: 252px; }
  .contact--phone { top: 318px; }
  .contact--phone .contact__text { padding-left: 50px; }

  .web {
    position: absolute; left: 58px; top: 394px;
    font-size: 19px; font-weight: 700; color: var(--paper);
    display: flex; align-items: center; gap: 16px;
  }
  .web svg { width: 18px; height: 18px; }
</style>
</head>
<body>

<section class="card card--front" aria-label="Business card front">
  <svg class="card__shapes" viewBox="0 0 760 455" aria-hidden="true">
    <defs>
      <linearGradient id="bandFade" x1="0" x2="1" y1="0" y2="0">
        <stop offset="0" stop-color="#F0912C"/>
        <stop offset=".72" stop-color="#F0912C"/>
        <stop offset="1" stop-color="#FBE8D2"/>
      </linearGradient>
    </defs>
    <rect class="web-band" x="0" y="370" width="560" height="73" fill="url(#bandFade)"/>
    <path class="arc arc--green" d="M545,0 C440,70 378,170 394,255 C410,345 525,420 665,455 L760,455 L760,0 Z" fill="#59FF00"/>
    <path class="arc arc--blue" d="M598,0 C492,62 425,160 432,245 C440,330 520,410 640,455 L760,455 L760,0 Z" fill="#0094D4"/>
    <path class="arc arc--white" d="M659,0 C560,52 486,150 492,245 C498,330 562,405 628,455 L760,455 L760,0 Z" fill="#ffffff"/>
  </svg>

  <div class="brand"><span class="brand__dot"></span>Cedar Brook<br>Stables, LLC</div>

  <div class="person">
    <div class="person__name">YOUR NAME</div>
    <div class="person__role">Director/C.E.O</div>
  </div>
  <div class="divider"></div>

  <div class="contact contact--address">
    <svg viewBox="0 0 20 20" aria-hidden="true"><circle cx="10" cy="10" r="9" fill="#F0912C"/><path d="M10 4.5a3.5 3.5 0 0 0-3.5 3.5c0 2.6 3.5 6.5 3.5 6.5s3.5-3.9 3.5-6.5A3.5 3.5 0 0 0 10 4.5z" fill="#fff"/><circle cx="10" cy="8" r="1.3" fill="#F0912C"/></svg>
    <span class="contact__text">218 Pinecrest Ln,<br>Aiken,29801</span>
  </div>
  <div class="contact contact--phone">
    <svg viewBox="0 0 20 20" aria-hidden="true"><circle cx="10" cy="10" r="9" fill="#F0912C"/><path d="M7 5.5l1.6 2.6-1 1.1c.7 1.4 1.7 2.4 3.1 3.1l1.1-1 2.6 1.6-.8 1.7c-3.6-.3-7-3.7-7.3-7.3z" fill="#fff"/></svg>
    <span class="contact__text">(803) 555-0142</span>
  </div>

  <div class="web">
    <svg viewBox="0 0 18 18" aria-hidden="true"><circle cx="9" cy="9" r="7.5" fill="none" stroke="#fff" stroke-width="1.6"/><ellipse cx="9" cy="9" rx="3.2" ry="7.5" fill="none" stroke="#fff" stroke-width="1.3"/><path d="M1.5 9h15M3 5h12M3 13h12" stroke="#fff" stroke-width="1.2"/></svg>
    <span>http://www.cedarbrookstables.com</span>
  </div>
</section>

<section class="card card--back" aria-label="Business card back">
  <svg class="card__shapes" viewBox="0 0 760 455" aria-hidden="true">
    <path class="arc arc--orange" d="M0,40 C95,95 128,220 112,330 C100,400 55,440 20,455 L0,455 Z" fill="#F0912C"/>
    <path class="arc arc--blue" d="M0,150 C60,210 75,290 65,360 C58,410 35,440 15,455 L0,455 Z" fill="#0094D4"/>
    <path class="arc arc--white" d="M0,95 C62,150 85,240 74,320 C66,380 35,425 0,455 Z" fill="#ffffff"/>

    <path class="arc arc--orange" d="M760,95 C650,130 600,230 612,320 C622,385 665,430 700,455 L760,455 Z" fill="#F0912C"/>
    <path class="arc arc--green" d="M760,108 C688,140 650,230 660,315 C668,380 700,430 730,455 L760,455 Z" fill="#59FF00"/>
    <path class="arc arc--white" d="M760,150 C705,180 680,250 688,320 C695,380 720,425 745,455 L760,455 Z" fill="#ffffff"/>
  </svg>

  <div class="brand"><span class="brand__dot"></span>Cedar Brook<br>Stables, LLC</div>
</section>

</body>
</html>
```